One-page magazine ad for accountant serving the non-profit industry

I am Certified Public Accountant placing a one-page ad in Harvestlight Journal. The ad will be seen by churches and other non-profit organizations.
Harvestlight Journal requires the following:
Accepted file formats:
a) Press ready PDF with all fonts embedded. OR
b) Flattened CMYK Abode Photoshop PSD or illustrator PDF or EPS with all fonts outlined.
Ad Specs:
Trim 8" x 10.5"
Live 7.5" x 10"
Bleed 8.25" x 10.75"

I would like the ad to state the following information:

Marcus T. Velloway, CPA, CGMA

I am Certified Public Accountant with over 30 years of experience serving the accounting and tax needs of churches and non-profit organizations.

Some of the services I can offer:

Audits, Reviews, Compilations
Bookkeeping Services
Payroll Taxes
501C3 - IRS exemption applications
Clergy Housing Allowance issues and Personal Taxes

```html
<!DOCTYPE html>
<html lang="en">
<head>
<meta charset="UTF-8">
<title>Accounting &amp; Tax Services — Marcus T. Velloway, CPA, CGMA</title>
<link rel="stylesheet" href="https://fonts.googleapis.com/css2?family=Saira+Condensed:wght@700&family=Encode+Sans+Expanded:wght@400;700&display=swap">
<style>
  :root {
    --bg: #0a1ee8;
    --headline: #6f8ff2;
    --text: #ffffff;
    --bar-1: #1b2ef0;
    --bar-2: #3449ee;
    --bar-3: #4b64ee;
    --bar-4: #6681ef;
    --bar-5: #7d98f2;
  }
  * { margin: 0; padding: 0; box-sizing: border-box; }
  html, body { width: 914px; height: 1200px; overflow: hidden; background: var(--bg); }
  .ad {
    position: relative;
    width: 914px;
    height: 1200px;
    background: var(--bg);
    color: var(--text);
    font-family: "Encode Sans Expanded", "Helvetica Neue", Arial, sans-serif;
    overflow: hidden;
  }
  .growth-chart { position: absolute; left: 0; top: 0; width: 914px; height: 1200px; }
  .headline {
    position: absolute;
    left: 100px;
    top: 62px;
    font-family: "Saira Condensed", "Arial Narrow", sans-serif;
    font-weight: 700;
    font-size: 66px;
    line-height: 1;
    letter-spacing: 1.5px;
    color: var(--headline);
    white-space: nowrap;
  }
  .advisor-name {
    position: absolute;
    left: 105px;
    top: 196px;
    font-weight: 700;
    font-size: 29px;
    letter-spacing: 0.8px;
    white-space: nowrap;
  }
  .intro {
    position: absolute;
    left: 105px;
    top: 258px;
    width: 720px;
    font-size: 21px;
    line-height: 39px;
    letter-spacing: 0.6px;
  }
  .services {
    position: absolute;
    left: 106px;
    top: 410px;
    list-style: none;
  }
  .services li {
    position: relative;
    padding-left: 28px;
    height: 57px;
    font-size: 19px;
    line-height: 28px;
    letter-spacing: 1px;
    text-transform: uppercase;
    white-space: nowrap;
  }
  .services li::before {
    content: "";
    position: absolute;
    left: 0;
    top: 10px;
    width: 8px;
    height: 8px;
    background: var(--text);
  }
  .contact {
    position: absolute;
    left: 105px;
    top: 822px;
    font-size: 21px;
    line-height: 51px;
    letter-spacing: 0.8px;
  }
  .contact a { color: inherit; text-decoration: none; display: block; }
</style>
</head>
<body>
  <main class="ad">
    <svg class="growth-chart" viewBox="0 0 914 1200" aria-hidden="true">
      <rect x="32"  y="1097" width="130" height="103" fill="var(--bar-1)"/>
      <rect x="212" y="997"  width="130" height="203" fill="var(--bar-2)"/>
      <rect x="392" y="884"  width="130" height="316" fill="var(--bar-3)"/>
      <rect x="572" y="700"  width="130" height="500" fill="var(--bar-4)"/>
      <rect x="751" y="468"  width="130" height="732" fill="var(--bar-5)"/>
    </svg>

    <h1 class="headline">ACCOUNTING &amp; TAX SERVICES</h1>
    <h2 class="advisor-name">Marcus T. Velloway, CPA, CGMA</h2>
    <p class="intro">Certified Public Accountant with over 30 years<br>of experience serving the accounting and tax<br>needs of churches and non-profit organizations.</p>

    <ul class="services">
      <li>Audits, Reviews, Compilations</li>
      <li>Bookkeeping Services</li>
      <li>Payroll Taxes</li>
      <li>501C3 — IRS Exemption Applications</li>
      <li>Clergy Housing Allowance Issues</li>
      <li>Personal Taxes</li>
    </ul>

    <address class="contact">
      <a href="mailto:marcus@vellowaycpa.com">marcus@vellowaycpa.com</a>
      <a href="tel:5165550142">516-555-0142</a>
    </address>
  </main>
</body>
</html>
```